Stylise 5 diagrams to feature on webpage

We need existing diagrams recreated in a stylized format to go on our web page.

We will provide all required drafts and are after a style/design set which will work with our brand identity, target market and existing website.

Company Background
- We are a provider of data, software and services which blue chip companies use to shape their customer experience. ie very high tier companies, so our audience are of a high calibre.

What we want to present is clarity of thought, expertise and authority (ie we deal in data so a certain amount of conservatism is required to inspire trust in our data). However we dont want this to appear old and 'stuffy'. We want to present as the savvy partner who know their stuff but at the same time are modern and innovative and fresh.
So I am imagining crisp, clean, slick and innovative.

Potential for ongoing work
This project will have a number of images to recreate initially. However we will need an ongoing service/provider which can duplicate the style.
Other pieces may include designing PPT templates, presentations, reports, web, brochures etc

Website that the diagrams will live within.
http://new.quillbrookdata.com.au/ this is the start of the new web page. the images will sit inside the content and will need to 'balance' the currently high text to image ratio and work with the existing logo and style.
Please don't let the existing website limit your creativity or inspiration - we are open to improving our design elements :) What I do want to retain in alignment with the website is simplicity and 'crisp', ie use of clean fonts and sharp colours.

Attached are our existing brand guides. Again, please observe these loosely but feel free to offer up any improvements. The key here is that the Aubergine key colour is respected.

NOTE: Both attached files are the same but in different formats as some were having troubles opening.

Target Market(s)

Target Market(s)
- Executives of large blue chip companies (think airlines, telcos, etc).
- Consulting firms (think Halvering Marchbank, TBRW, Fenmoor)

Industry/Entity Type

Software

Requirements
Must have
• Must haves
- PSD editable format for text, graphics, all elements
- the diagrams required must look to be of the same design 'family'. Once we establish this style we can progress to develop all the required diagrams and in future create a rship where we develop additional company collateral

```html
<!DOCTYPE html>
<html lang="en">
<head>
<meta charset="utf-8">
<title>Customer Experience Cycle and Net Promoter Score</title>
<link rel="stylesheet" href="https://fonts.googleapis.com/css2?family=PT+Sans:wght@400;700&display=swap">
<style>
  :root {
    --aubergine: #9b1f55;
    --aubergine-light: #b8407a;
    --aubergine-dark: #7a1441;
    --steel: #a4a4a6;
    --steel-light: #c4c4c6;
    --steel-dark: #838386;
    --passive: #f1c40f;
    --promoter: #1f8a3c;
    --ink: #6f6f71;
    --track: #e2e2e4;
    --track-edge: #c9c9cc;
    --white: #ffffff;
  }
  * { margin: 0; padding: 0; box-sizing: border-box; }
  html, body { width: 1200px; height: 1004px; overflow: hidden; background: var(--white); }
  body { font-family: "PT Sans", Arial, sans-serif; position: relative; }

  .cycle { position: absolute; left: 0; top: 0; width: 1200px; height: 600px; }
  .cycle-label { font-weight: 700; font-size: 36px; fill: var(--white); letter-spacing: 0.5px; }

  .nps { position: absolute; left: 0; top: 640px; width: 1200px; height: 364px; }

  .segment-figures {
    position: absolute; top: 22px; height: 175px;
    border-radius: 70px 70px 0 0;
  }
  .segment-figures.detractors { left: 146px; width: 462px; background: linear-gradient(90deg, var(--aubergine) 0 36%, #7d7d80 36%, #9d9d9f 100%); }
  .segment-figures.passives   { left: 630px; width: 170px; background: linear-gradient(90deg, var(--passive) 0 62%, #8a8a8c 62%, #9d9d9f 100%); }
  .segment-figures.promoters  { left: 862px; width: 162px; background: linear-gradient(90deg, var(--promoter) 0 68%, #8a8a8c 68%, #9d9d9f 100%); }

  .segment-name {
    position: absolute; top: 147px;
    font-weight: 700; font-size: 25px; color: var(--white);
  }
  .segment-name.detractors { left: 152px; }
  .segment-name.passives   { left: 656px; }
  .segment-name.promoters  { left: 872px; }

  .score-track {
    position: absolute; left: 115px; top: 190px; width: 970px; height: 62px;
    border-radius: 14px;
    background: linear-gradient(180deg, #f4f4f5 0%, var(--track) 55%, var(--track-edge) 100%);
    box-shadow: inset 0 -2px 3px rgba(0,0,0,0.12);
  }
  .score {
    position: absolute; top: 206px; width: 40px; margin-left: -20px;
    text-align: center; font-weight: 700; font-size: 25px; line-height: 30px;
  }
  .score.detractor { color: var(--aubergine-dark); }
  .score.passive   { color: var(--passive); }
  .score.promoter  { color: var(--promoter); }

  .formula {
    position: absolute; top: 276px; left: 0; width: 1200px;
    text-align: center; font-weight: 700; font-size: 29px; color: var(--ink);
    word-spacing: 4px;
  }
  .formula .equals { margin: 0 22px; }
  .formula .plus { margin: 0 18px; }
  .formula .term-promoters { color: var(--promoter); }
  .formula .term-detractors { color: var(--aubergine-dark); }
</style>
</head>
<body>

<svg class="cycle" viewBox="0 0 1200 600" aria-label="Listen, Act, Discover, Improve cycle">
  <defs>
    <linearGradient id="aubergine-fill" x1="0" y1="0" x2="1" y2="1">
      <stop offset="0" stop-color="var(--aubergine-light)"/>
      <stop offset="1" stop-color="var(--aubergine-dark)"/>
    </linearGradient>
    <linearGradient id="steel-fill" x1="0" y1="0" x2="1" y2="1">
      <stop offset="0" stop-color="var(--steel-light)"/>
      <stop offset="1" stop-color="var(--steel-dark)"/>
    </linearGradient>
    <filter id="segment-shadow" x="-20%" y="-20%" width="140%" height="140%">
      <feDropShadow dx="0" dy="3" stdDeviation="4" flood-color="#000" flood-opacity="0.25"/>
    </filter>
  </defs>

  <g class="cycle-segments" filter="url(#segment-shadow)" stroke="var(--white)" stroke-width="3" stroke-linejoin="round">
    <path class="segment-improve" fill="url(#steel-fill)"
      d="M362 285 A238 238 0 0 1 600 47 L638.3 105 L600 155 A130 130 0 0 0 470 285 L420 246.7 Z"/>
    <path class="segment-act" fill="url(#steel-fill)"
      d="M838 285 A238 238 0 0 1 600 523 L561.7 465 L600 415 A130 130 0 0 0 730 285 L780 323.3 Z"/>
    <path class="segment-discover" fill="url(#aubergine-fill)"
      d="M600 523 A238 238 0 0 1 362 285 L420 246.7 L470 285 A130 130 0 0 0 600 415 L561.7 465 Z"/>
    <path class="segment-listen" fill="url(#aubergine-fill)"
      d="M600 47 A238 238 0 0 1 838 285 L780 323.3 L730 285 A130 130 0 0 0 600 155 L638.3 105 Z"/>
  </g>

  <text class="cycle-label" x="730" y="155" text-anchor="middle" dominant-baseline="middle" transform="rotate(50 730 155)">Listen</text>
  <text class="cycle-label" x="730" y="415" text-anchor="middle" dominant-baseline="middle" transform="rotate(-48 730 415)">Act</text>
  <text class="cycle-label" x="470" y="415" text-anchor="middle" dominant-baseline="middle" transform="rotate(45 470 415)">Discover</text>
  <text class="cycle-label" x="470" y="155" text-anchor="middle" dominant-baseline="middle" transform="rotate(-50 470 155)">Improve</text>
</svg>

<section class="nps">
  <div class="segment-figures detractors" role="img" aria-label="Row of customer silhouettes representing detractors"></div>
  <div class="segment-figures passives" role="img" aria-label="Customer silhouettes representing passives"></div>
  <div class="segment-figures promoters" role="img" aria-label="Customer silhouettes representing promoters"></div>

  <span class="segment-name detractors">Detractors</span>
  <span class="segment-name passives">Passives</span>
  <span class="segment-name promoters">Promoters</span>

  <div class="score-track"></div>
  <span class="score detractor" style="left:218px">0</span>
  <span class="score detractor" style="left:281px">1</span>
  <span class="score detractor" style="left:345px">2</span>
  <span class="score detractor" style="left:409px">3</span>
  <span class="score detractor" style="left:474px">4</span>
  <span class="score detractor" style="left:538px">5</span>
  <span class="score detractor" style="left:603px">6</span>
  <span class="score passive" style="left:692px">7</span>
  <span class="score passive" style="left:757px">8</span>
  <span class="score promoter" style="left:912px">9</span>
  <span class="score promoter" style="left:978px">10</span>

  <p class="formula">Net Promoter Score<span class="equals">=</span><span class="term-promoters">%Promoters</span><span class="plus">+</span><span class="term-detractors">%Detractors</span></p>
</section>

</body>
</html>
```